Halvek Insurance Stationery Design Project

We need a stationery design for business cards, letterhead and envelopes.

Please refer to attached brief for further information.

Business

```html
<!DOCTYPE html>
<html lang="en">
<head>
<meta charset="utf-8">
<title>Halvek Insurance Stationery</title>
<link href="https://fonts.googleapis.com/css2?family=Mulish:wght@400;600;700&display=swap" rel="stylesheet">
<style>
:root{
  --navy:#1e3a52;
  --orange:#f47920;
  --grey:#555b61;
  --paper:#ffffff;
  --backdrop:#e6e4e1;
  --card-dark:#1d3a53;
}
*{margin:0;padding:0;box-sizing:border-box}
html,body{width:1200px;height:900px;overflow:hidden}
body{background:var(--backdrop);font-family:"Mulish",Arial,sans-serif;color:var(--navy);position:relative}
.sheet{position:absolute;background:var(--paper);box-shadow:0 3px 10px rgba(0,0,0,.25)}
.brand-name{position:absolute;font-weight:700;color:var(--navy);letter-spacing:.2px;line-height:1;white-space:nowrap}
.brand-name--light{color:#fff}
.tagline{position:absolute;font-weight:700;color:var(--navy);white-space:nowrap}

.letterhead-back{left:34px;top:80px;width:250px;height:792px}
.letterhead{left:184px;top:28px;width:612px;height:792px}
.letterhead .contact{position:absolute;right:24px;top:34px;text-align:right;font-size:8.6px;line-height:10.6px;color:var(--grey);font-style:normal}
.letterhead .contact .web{color:var(--orange);font-weight:700}
.letterhead .legal{position:absolute;left:0;right:0;top:734px;text-align:center;font-size:5.4px;line-height:7px;color:var(--grey)}
.letterhead .copyright{position:absolute;left:0;right:0;top:770px;text-align:center;font-size:5.4px;font-weight:700;color:var(--navy)}

.card-front{left:822px;top:80px;width:252px;height:146px;overflow:hidden}
.card-front .person{position:absolute;left:17px;top:60px}
.card-front .person-name{font-size:10px;font-weight:700}
.card-front .person-role{font-size:7px;font-weight:700;color:var(--orange)}
.card-front .address{position:absolute;left:17px;top:94px;font-size:5.4px;line-height:7.4px;color:var(--grey)}
.card-front .lines{position:absolute;left:114px;top:95px;font-size:5.4px;line-height:7.6px;color:var(--grey)}
.card-front .lines li{list-style:none;display:flex;align-items:center;gap:4px}
.card-front .lines svg{width:6px;height:6px;fill:var(--navy)}
.card-front .stripe{position:absolute;left:0;right:0;top:127px;height:3px;background:var(--orange)}
.card-front .web-band{position:absolute;left:0;right:0;top:130px;height:16px;background:var(--navy);color:#fff;font-size:6.5px;font-weight:700;text-align:center;line-height:16px}

.card-back{left:822px;top:244px;width:252px;height:144px;background:var(--card-dark);overflow:hidden}
.card-back .brand-name{left:0;right:0;text-align:center}
.card-back .legal{position:absolute;left:8px;right:8px;top:119px;text-align:center;font-size:4.2px;line-height:5.8px;color:#c9d3dc}

.envelope{left:454px;top:424px;width:684px;height:296px}
.envelope .recipient{position:absolute;left:463px;top:234px;font-size:11px;line-height:12.5px;color:var(--navy)}
.envelope .recipient strong{font-weight:700}
</style>
</head>
<body>

<section class="sheet letterhead-back" aria-label="Letterhead, second sheet">
  <p class="brand-name" style="left:32px;top:40px;font-size:20px">Halvek Insurance</p>
</section>

<section class="sheet letterhead" aria-label="Letterhead">
  <p class="brand-name" style="left:38px;top:44px;font-size:28px">Halvek Insurance</p>
  <p class="tagline" style="left:52px;top:93px;font-size:10px">Business and Life Insurance Brokers and Advisers</p>
  <address class="contact">
    Level 4, 18 Carrow St<br>Northgate NSW 2061<br>PO Box 418<br>Northgate NSW 2062<br>
    <span style="display:block;margin-top:2px">Ph: (02) 5550 1840</span>Fax: (02) 5550 1841<br>
    Email: info@halvekinsurance.example<br><span class="web">www.halvekinsurance.example</span>
  </address>
  <p class="legal">Halvek Insurance Holdings Pty Ltd ABN 41 902 118 604 is an Authorised Representative of Corvane Adviser Network Pty Limited<br>
  Authorised Representative No. 402118 &nbsp;&nbsp;|&nbsp;&nbsp; Australian Financial Services No. 251730<br>
  Corvane Financial Services Pty Ltd and its advisers are members of Tallis Financial<br>
  Advisers and Authorised Representatives of Brackwell Advice Group Pty Ltd AFSL 247713</p>
  <p class="copyright">Copyright 2012 Halvek Insurance Holdings Pty Ltd. All rights reserved.</p>
</section>

<section class="sheet card-front" aria-label="Business card, front">
  <p class="brand-name" style="left:16px;top:13px;font-size:13px">Halvek Insurance</p>
  <p class="tagline" style="left:16px;top:38px;font-size:5.6px">Business and Life Insurance Brokers and Advisers</p>
  <div class="person"><p class="person-name">Marcus Halvek</p><p class="person-role">Director</p></div>
  <p class="address">Level 4, 18 Carrow St<br>Northgate NSW 2061<br>PO Box 418<br>Northgate NSW 2062</p>
  <ul class="lines">
    <li><svg viewBox="0 0 10 10"><path d="M2 0h2l1 3-1.5 1a6 6 0 0 0 2.5 2.5L7 5l3 1v2a2 2 0 0 1-2 2A8 8 0 0 1 0 2a2 2 0 0 1 2-2z"/></svg>(02) 5550 1840</li>
    <li><svg viewBox="0 0 10 10"><rect x="0" y="3" width="10" height="5" rx="1"/><rect x="2" y="0" width="6" height="3"/></svg>(02) 5550 1841</li>
    <li><svg viewBox="0 0 10 10"><rect x="2.5" y="0" width="5" height="10" rx="1"/></svg>0400 555 219</li>
    <li><svg viewBox="0 0 10 10"><rect x="0" y="2" width="10" height="6" rx="1"/></svg>mhalvek@halvekinsurance.example</li>
  </ul>
  <div class="stripe"></div>
  <p class="web-band">www.halvekinsurance.example</p>
</section>

<section class="sheet card-back" aria-label="Business card, back">
  <p class="brand-name brand-name--light" style="top:57px;font-size:18px">Halvek Insurance</p>
  <p class="legal">Authorised Representative No. 402118 &nbsp;|&nbsp; Corvane Adviser Network Pty Limited AFSL 251730<br>
  Corvane Financial Services Pty Ltd and its advisers are members of Tallis Financial Advisers<br>
  and Authorised Representatives of Brackwell Advice Group Pty Ltd AFSL 247713</p>
</section>

<section class="sheet envelope" aria-label="Envelope">
  <p class="brand-name" style="left:38px;top:30px;font-size:28px">Halvek Insurance</p>
  <p class="tagline" style="left:38px;top:76px;font-size:10.5px">Business and Life Insurance Brokers and Advisers</p>
  <p class="recipient"><strong>Halvek Insurance Holdings Pty Ltd</strong><br>PO Box 418<br>Northgate NSW 2062</p>
</section>

</body>
</html>
```